Epoxy coatings company needs a logo/business card design.

My company name is "Lustrous Resin Works", and I am looking for a company logo and business card design.
My initial thought was to use "Æ"in 'Lu'strous, and would also like to see ideas on how to play around with the fact that the first 3 letters (Lrw) are also the acronym of the company name.
I specialize in garage floor and interior epoxy coatings, paint flake broadcasts, quartz broadcasts, and solid color epoxy floors, concrete repairs.
I like images I've seen of a silhouetted person running a floor grinder. It keeps the design of the card simple. I'm not necessarily opposed to using images of the floors on the card, but I'd prefer to keep the front simple (Company name, my name, phone number, email) and maybe put pictures on the back. I've included a few of my personal pictures of floors I've done (including a before, after, and when the garage was being used after)
My colors are darker green (Fern/Forest/Hunter, etc), and Bronze.

Contact Information for Business Card

Name: Dana Kellworth Email: lustrousresinworks@mailbrook.net Phone: (555)318-9042 Instagram: lustrous_resin_works

Colors

Designer to choose colors to be used in the design.

Requirements
Nice to have
• I've included a business card designed for someone else, that contains the silhouette that I'm looking for. The floor grinder that I use is large like the one pictured (Torvex G40R).

```html
<!DOCTYPE html>
<html lang="en">
<head>
<meta charset="utf-8">
<title>Lustrous Resin Works — Business Card</title>
<link href="https://fonts.googleapis.com/css2?family=Archivo:wght@400;500;700;800&display=swap" rel="stylesheet">
<style>
  :root {
    --bg: #d4d4d4;
    --card-white: #ffffff;
    --forest: #173006;
    --text-gray: #555555;
    --label-white: #f4f4f4;
    --grinder-tone: linear-gradient(135deg, #c9cbcd 0%, #9fa3a7 50%, #6c7075 100%);
    --before-tone: linear-gradient(160deg, #b8b8b6 0%, #8d8d8a 55%, #cfcfcc 100%);
    --after-tone: linear-gradient(160deg, #3d3a33 0%, #6f7680 45%, #8a95a3 100%);
  }
  * { box-sizing: border-box; margin: 0; padding: 0; }
  html, body { width: 1200px; height: 800px; overflow: hidden; }
  body {
    background: var(--bg);
    font-family: "Archivo", Arial, sans-serif;
    position: relative;
  }
  .card {
    position: absolute;
    top: 245px;
    width: 540px;
    height: 309px;
    border-radius: 24px;
    overflow: hidden;
    box-shadow: 0 10px 24px rgba(0,0,0,0.18);
  }
  .card-front { left: 40px; background: var(--card-white); }
  .card-back { left: 620px; background: var(--forest); }

  .company-mark {
    position: absolute;
    left: 38px; top: 30px;
    width: 150px;
    display: flex; align-items: flex-start; gap: 8px;
  }
  .company-dot {
    width: 12px; height: 12px; flex: none;
    margin-top: 4px;
    border-radius: 50%;
    background: var(--forest);
  }
  .company-name {
    font-weight: 800;
    font-size: 17px;
    line-height: 20px;
    letter-spacing: 0.04em;
    text-transform: uppercase;
    color: var(--forest);
  }

  .grinder-image {
    position: absolute;
    left: 200px; top: 16px;
    width: 310px; height: 128px;
    border-radius: 10px;
    background: var(--grinder-tone);
  }
  .front-details {
    position: absolute;
    left: 38px; top: 152px;
    right: 30px;
  }
  .holder-name {
    font-weight: 800;
    font-size: 22px;
    letter-spacing: 0.06em;
    color: var(--forest);
    text-transform: uppercase;
    line-height: 1.1;
    margin-bottom: 5px;
  }
  .contact-list { list-style: none; margin-bottom: 6px; }
  .contact-item {
    display: flex; align-items: center; gap: 7px;
    font-size: 12.5px; color: var(--text-gray);
    line-height: 16px;
  }
  .contact-icon { width: 11px; height: 11px; flex: none; }
  .specialty-heading {
    font-weight: 800; font-size: 13px; letter-spacing: 0.03em;
    color: var(--forest); text-transform: uppercase;
    margin-bottom: 2px;
  }
  .specialty-text {
    font-size: 12.5px; color: var(--text-gray); line-height: 15.5px;
  }

  .gallery {
    position: absolute;
    left: 40px; right: 40px; top: 40px;
    display: flex; gap: 10px;
  }
  .gallery-item { flex: 1; text-align: center; }
  .gallery-photo { height: 200px; border-radius: 12px; }
  .photo-before { background: var(--before-tone); }
  .photo-after { background: var(--after-tone); }
  .gallery-label {
    margin-top: 12px;
    color: var(--label-white);
    font-weight: 700; font-size: 16px; letter-spacing: 0.02em;
  }
</style>
</head>
<body>
  <section class="card card-front" aria-label="Business card front">
    <div class="company-mark">
      <span class="company-dot" aria-hidden="true"></span>
      <p class="company-name">Lustrous<br>Resin Works</p>
    </div>
    <div class="grinder-image" role="img" aria-label="Large floor grinder, Torvex G40R"></div>
    <div class="front-details">
      <h1 class="holder-name">Dana Kellworth</h1>
      <ul class="contact-list">
        <li class="contact-item">
          <svg class="contact-icon" viewBox="0 0 12 12" aria-hidden="true"><path d="M3 1.2 L4.6 3.4 L3.6 4.6 C4.2 6 5.6 7.6 7.2 8.4 L8.4 7.4 L10.8 9 L9.8 10.8 C6 10.8 1.2 6 1.2 2.2 Z" fill="var(--forest)"/></svg>
          (555)318-9042
        </li>
        <li class="contact-item">
          <svg class="contact-icon" viewBox="0 0 12 12" aria-hidden="true"><rect x="0.5" y="2" width="11" height="8" fill="var(--forest)"/><path d="M0.8 2.4 L6 6.6 L11.2 2.4" stroke="#fff" stroke-width="1.1" fill="none"/></svg>
          lustrousresinworks@mailbrook.net
        </li>
        <li class="contact-item">
          <svg class="contact-icon" viewBox="0 0 12 12" aria-hidden="true"><circle cx="6" cy="6" r="5" fill="none" stroke="var(--forest)" stroke-width="1.4"/></svg>
          lustrous_resin_works
        </li>
      </ul>
      <h2 class="specialty-heading">Specializing in</h2>
      <p class="specialty-text">garage floor &amp; interior epoxy coatings<br>paint flake broadcasts, quartz broadcasts, &amp;<br>solid color epoxy floors, concrete repairs.</p>
    </div>
  </section>

  <section class="card card-back" aria-label="Business card back">
    <div class="gallery">
      <figure class="gallery-item">
        <div class="gallery-photo photo-before" role="img" aria-label="Stained bare concrete garage floor before coating"></div>
        <figcaption class="gallery-label">Before</figcaption>
      </figure>
      <figure class="gallery-item">
        <div class="gallery-photo photo-after" role="img" aria-label="Finished flake epoxy garage floor with a parked white car"></div>
        <figcaption class="gallery-label">After</figcaption>
      </figure>
    </div>
  </section>
</body>
</html>
```